Harold Brisk Mechanical business cards

We need business cards designed for "Harold Brisk Mechanical" "Mechanical & Electrical Contractors" "Specializing in Service & Installation"
"Cooling, Heating, Service, Installations, Residential, Commercial"

```html
<!DOCTYPE html>
<html lang="en">
<head>
<meta charset="utf-8">
<title>Harold Brisk Mechanical – Business Cards</title>
<link href="https://fonts.googleapis.com/css2?family=Lato:wght@400;700;900&display=swap" rel="stylesheet">
<style>
  :root {
    --backdrop: #3a3b3e;
    --card-dark: #1b1b1c;
    --card-light: #ffffff;
    --brand-red: #e3232b;
    --ink: #1e1e1e;
    --ink-soft: #2c2c2c;
    --rule-dark: #6a6a6a;
    --rule-light: #8a8a8a;
  }
  * { box-sizing: border-box; margin: 0; padding: 0; }
  html, body {
    width: 1200px; height: 900px; overflow: hidden;
    background: var(--backdrop);
    font-family: "Lato", Arial, sans-serif;
  }
  .stage { position: relative; width: 1200px; height: 900px; }

  .card {
    position: absolute;
    width: 560px; height: 320px;
    border-radius: 22px;
    overflow: hidden;
  }

  /* Front (dark) card */
  .card--front {
    left: 70px; top: 110px;
    background: var(--card-dark);
    color: #fff;
  }
  .card--front .front-brand {
    position: absolute; left: 0; right: 0; top: 70px;
    display: flex; justify-content: center; align-items: center; gap: 14px;
  }
  .card--front .front-rule {
    position: absolute; left: 80px; right: 80px; top: 178px;
    height: 1px; background: var(--rule-dark);
  }
  .card--front .services {
    position: absolute; left: 60px; right: 40px; top: 198px;
    list-style: none;
    font-size: 15px; line-height: 1.6;
    color: #f2f2f2;
  }
  .services li { display: flex; align-items: center; gap: 10px; }
  .services .bullet {
    width: 11px; height: 11px; background: var(--brand-red); flex: none;
  }
  .services li.indent { padding-left: 22px; }
  .card--front .stripe {
    position: absolute; left: 0; right: 0; bottom: 0;
    height: 12px; background: var(--brand-red);
  }

  /* Brand name lockup */
  .brand-mark {
    width: 34px; height: 34px; background: var(--brand-red); flex: none;
  }
  .brand-name {
    font-weight: 900; font-size: 26px; line-height: 1.1;
    letter-spacing: 1px; text-transform: uppercase;
  }
  .card--front .brand-name { color: #ffffff; }
  .card--back .brand-name { color: var(--ink); }

  /* Back (light) card */
  .card--back {
    left: 570px; top: 470px;
    background: var(--card-light);
    color: var(--ink);
    box-shadow: 0 6px 0 #111;
  }
  .card--back .back-brand {
    position: absolute; left: 36px; top: 126px; width: 230px;
    display: flex; align-items: center; gap: 12px;
  }
  .card--back .back-brand .brand-name { font-size: 22px; }
  .card--back .back-divider {
    position: absolute; left: 282px; top: 58px;
    width: 1px; height: 204px; background: var(--rule-light);
  }
  .contact {
    position: absolute; left: 306px; top: 62px; right: 20px;
    font-size: 14px; line-height: 1.35; color: var(--ink-soft);
  }
  .contact .person {
    color: var(--brand-red); font-weight: 900; font-size: 20px;
    text-transform: uppercase; line-height: 1.1;
  }
  .contact .role { font-size: 14px; margin-bottom: 18px; }
  .contact .address { margin-bottom: 16px; }
  .contact .lines { list-style: none; }
  .contact .lines li { display: flex; align-items: center; gap: 8px; }
  .contact .lines svg { width: 13px; height: 13px; flex: none; }
</style>
</head>
<body>
<main class="stage">

  <section class="card card--front" aria-label="Business card front">
    <div class="front-brand">
      <span class="brand-mark"></span>
      <span class="brand-name">Harold Brisk<br>Mechanical</span>
    </div>
    <div class="front-rule"></div>
    <ul class="services">
      <li><span class="bullet"></span>Mechanical &amp; Electrical Contractors</li>
      <li class="indent"><span class="bullet"></span>Specializing in Service &amp; Installation</li>
      <li class="indent"><span class="bullet"></span>Servicing Residential, Commercial and Industrial</li>
    </ul>
    <div class="stripe"></div>
  </section>

  <section class="card card--back" aria-label="Business card back">
    <div class="back-brand">
      <span class="brand-mark"></span>
      <span class="brand-name">Harold Brisk<br>Mechanical</span>
    </div>
    <div class="back-divider"></div>
    <div class="contact">
      <p class="person">Peter Lowell</p>
      <p class="role">Founder &amp; CEO</p>
      <p class="address">42 Marsh Lane, London<br>EC2A 4NT</p>
      <ul class="lines">
        <li>
          <svg viewBox="0 0 16 16" aria-hidden="true"><path fill="#e3232b" d="M3.6 1.5l2.3 2.6-1.2 1.7c.9 2 2.4 3.5 4.4 4.5l1.7-1.2 2.6 2.3-1.4 2.1C6.8 13.2 2.8 9.2 1.5 3z"/></svg>
          020 555 0142
        </li>
        <li>
          <svg viewBox="0 0 16 16" aria-hidden="true"><rect x="1" y="3" width="14" height="10" fill="#e3232b"/><path d="M1 3l7 6 7-6" fill="none" stroke="#fff" stroke-width="1.4"/></svg>
          info@haroldbrisk.com
        </li>
        <li>
          <svg viewBox="0 0 16 16" aria-hidden="true"><circle cx="8" cy="8" r="6.5" fill="none" stroke="#e3232b" stroke-width="1.5"/><path d="M1.5 8h13M8 1.5c-3 3.5-3 9.5 0 13M8 1.5c3 3.5 3 9.5 0 13" fill="none" stroke="#e3232b" stroke-width="1.2"/></svg>
          www.haroldbrisk.com
        </li>
      </ul>
    </div>
  </section>

</main>
</body>
</html>
```